Wix Website

I would like to migrate my current website (www.meadowlarkprep.com) over to a Wix template. Right now, I think my site is too playful. I am looking for a really clean, modern and updated feel. I still want a classical feel. Simple the better. As for what we do, we are a provider of in-home tutoring. We service young to old. students alike. Looking for something academic but not pre-school. A good balance of elementary to high school.

Looking also to scale down the site to as little pages as possible. Again, simple the better. Would like a really good home page and an even better landing page that highlights a quick and easy signup form.

Please feel free to get as much info off the current site to make the page. The final design should highlight "The Human Side of Tutoring". Please make sure our tagline of "Helping students and their parents live above the stress and strain of academic struggles" is prominent. Appropriate Stock photos are permissible at this time. We can change them as needed

```html
<!DOCTYPE html>
<html lang="en">
<head>
<meta charset="utf-8">
<title>Meadowlark Prep – In-Home Tutoring</title>
<link href="https://fonts.googleapis.com/css2?family=PT+Sans:wght@400;700&display=swap" rel="stylesheet">
<style>
  :root{
    --header-bg:#f4f5f7;
    --nav-text:#555659;
    --brand-red:#d8283f;
    --brand-orange:#d9772a;
    --brand-wine:#9b1b30;
    --bubble-grey:#6b6b6b;
    --tagline-bar:#a8a9ab;
    --panel:rgba(215,220,226,0.78);
    --form-bg:rgba(200,205,212,0.85);
    --field:#ffffff;
    --button:#6e6f71;
    --heading:#545558;
    --body-text:#3f4043;
    --rule:#8c8d90;
    --hero-shelf:#a4abb3;
    --hero-shirt:#b3cbe2;
    --hero-warm:#c6b6aa;
    --hero-sweater:#a9b8c4;
  }
  *{box-sizing:border-box;margin:0;padding:0}
  html,body{width:1200px;height:1000px;overflow:hidden}
  body{font-family:"PT Sans",Tahoma,sans-serif;background:#fff;position:relative}

  .site-header{position:absolute;left:0;top:0;width:1200px;height:78px;background:var(--header-bg);border-bottom:1px solid #e2e4e8}
  .brand{position:absolute;left:128px;top:18px;display:flex;align-items:center;gap:10px}
  .brand-dot{width:34px;height:34px;border-radius:50%;background:var(--brand-orange)}
  .brand-name{font-size:28px;font-weight:700;color:var(--brand-red);line-height:1}
  .main-nav{position:absolute;right:124px;top:25px;display:flex;gap:20px;font-size:17px;color:var(--nav-text)}
  .main-nav a{color:inherit;text-decoration:none}

  .hero{position:absolute;left:0;top:78px;width:1200px;height:528px}
  .hero-photo{position:absolute;inset:0;background:linear-gradient(90deg,var(--hero-shelf) 0%,var(--hero-shirt) 40%,var(--hero-warm) 68%,var(--hero-sweater) 100%)}
  .signup-panel{position:absolute;left:125px;top:317px;width:950px;height:211px;background:var(--panel)}
  .tagline{position:absolute;left:5px;top:3px;width:940px;height:40px;background:var(--tagline-bar);color:#fff;font-size:20.5px;text-align:center;line-height:40px}
  .signup-form{position:absolute;left:5px;top:50px;width:535px;height:161px;background:var(--form-bg)}
  .field{position:absolute;background:var(--field);font-size:13px;color:#222;padding:8px 10px;height:29px}
  .submit{position:absolute;left:407px;top:112px;width:118px;height:38px;background:var(--button);border:1px solid #eee;color:#fff;font-size:15px;text-align:center;line-height:36px}

  .steps{position:absolute;left:580px;top:43px;width:370px;height:168px}
  .step{position:absolute;width:54px;height:54px;border-radius:50%;color:#fff;font-size:16px;display:flex;align-items:center;justify-content:center;text-align:center;line-height:1.1}
  .string{position:absolute;top:0;width:1px;background:#fff}

  .features{position:absolute;left:0;top:606px;width:1200px;height:394px;background:linear-gradient(#f3f4f6,#ffffff 60%)}
  .feature{position:absolute;top:44px;width:290px;text-align:center}
  .feature h2{font-size:25px;font-weight:400;color:var(--heading);margin-bottom:10px}
  .feature-art{width:96px;height:70px;margin:0 auto 16px}
  .feature p{font-size:13.4px;color:var(--body-text);line-height:16px;white-space:nowrap}

  .footer-rule{position:absolute;left:125px;top:939px;width:950px;height:1px;background:var(--rule)}
  .copyright{position:absolute;left:0;top:962px;width:1200px;text-align:center;font-size:12.5px;color:var(--body-text)}
</style>
</head>
<body>
  <header class="site-header">
    <div class="brand"><span class="brand-dot"></span><span class="brand-name">Meadowlark Prep</span></div>
    <nav class="main-nav">
      <a href="#">Home</a><a href="#">Our Story</a><a href="#">Our Tutoring</a><a href="#">FAQ</a><a href="#">Areas We Serve</a><a href="#">Contact Us</a><a href="#">Summer Tutoring</a>
    </nav>
  </header>

  <section class="hero">
    <div class="hero-photo" role="img" aria-label="Photo of a tutor and student smiling while studying together in front of a bookshelf"></div>
    <div class="signup-panel">
      <div class="tagline">Helping students and their parents live above the stress and strain of academic struggles.</div>
      <form class="signup-form">
        <div class="field" style="left:8px;top:6px;width:168px">Name*</div>
        <div class="field" style="left:184px;top:6px;width:168px">Phone*</div>
        <div class="field" style="left:361px;top:6px;width:168px">Email*</div>
        <div class="field" style="left:8px;top:42px;width:168px">City*</div>
        <div class="field" style="left:184px;top:42px;width:168px">&nbsp;Zip Code*</div>
        <div class="field" style="left:361px;top:42px;width:168px">Student's grade</div>
        <div class="field" style="left:8px;top:79px;width:388px;height:73px">Please describe your needs*</div>
        <div class="submit">Click &amp; Relax</div>
      </form>
      <div class="steps">
        <span class="string" style="left:34px;height:18px"></span>
        <span class="string" style="left:88px;height:78px"></span>
        <span class="string" style="left:173px;height:104px"></span>
        <span class="string" style="left:258px;height:78px"></span>
        <span class="string" style="left:312px;height:18px"></span>
        <div class="step" style="left:8px;top:14px;background:var(--bubble-grey)">What</div>
        <div class="step" style="left:62px;top:73px;background:var(--brand-orange)">Why</div>
        <div class="step" style="left:147px;top:99px;background:var(--brand-wine)">Who</div>
        <div class="step" style="left:232px;top:73px;background:var(--brand-orange)">How</div>
        <div class="step" style="left:286px;top:14px;background:var(--bubble-grey)">Let’s<br>Go!</div>
      </div>
    </div>
  </section>

  <section class="features">
    <div class="feature" style="left:133px">
      <h2>Get Help</h2>
      <div class="feature-art" role="img" aria-label="Illustration of the word help under a magnifying glass" style="background:linear-gradient(135deg,#f3f3f3,#e0242c 60%,#f5f5f5)"></div>
      <p>Is your child struggling in school and needs<br>help that you can’t provide? In home tutoring<br>from Meadowlark Prep provides the opportunity<br>for academic excellence while helping your<br>child build confidence through one on one<br>learning.</p>
    </div>
    <div class="feature" style="left:454px">
      <h2>Get Back On Track</h2>
      <div class="feature-art" role="img" aria-label="Illustration of small figures standing on circular arrows" style="background:linear-gradient(90deg,#4a8fc8,#8cbf3a 50%,#e98a2a)"></div>
      <p>Getting back on track is easy when your<br>struggling student is matched with the ideal<br>tutor that meets their needs. Our tutors are<br>not only passionate about their areas of ex-<br>pertise but they are passionate about your<br>child’s success.</p>
    </div>
    <div class="feature" style="left:763px">
      <h2>Get Results</h2>
      <div class="feature-art" role="img" aria-label="Illustration of a results chart under a magnifying glass" style="width:80px;background:linear-gradient(135deg,#f2f2f2,#c9d6c4 50%,#d94a4a)"></div>
      <p>Through the assistance tutoring provides,<br>your child will get results. You will see not<br>only academic improvements, but aslo in-<br>creased confidence and peace of mind. Let<br>Meadowlark Prep help your child soar!</p>
    </div>
  </section>

  <div class="footer-rule"></div>
  <footer class="copyright">© 2013 Meadowlark Prep, 888.555.0142</footer>
</body>
</html>
```